Marcus Lindqvist Photography needs a business card designs

I am looking for a business card with a logo clean and simple which I can use that logo on my website or on my pictures. It has to be very classy and very professional. Please look at my website at www.marcuslvqphoto.com for my signature. I'm thinking of something like that for my signature/logo. I'm still working on my website but you get an idea. I'm open to any design but not too busy graphics.

I will be printing the business card from qrivel.com.

Surprise me :)

contact me if you have any questions.

-ML

I'm receiving a lot of black background at the moment. I know my website is all black doesn't mean I want my card to be all black. Please send in with some white background as well. Thanks :)

check out some business cards that I found online. I think they are simple and look really awesome. I don't want a card that is too busy.

http://www.marcuslvqphoto.com/p270092084

Reason: Please extend the date for me. I haven't really receive any good design yet.

Printing

• -a logo that related to my first and last initial of my name "ML"
-double sided
• -I don't want my background to be all black.
-no pictures on the card

```html
<!DOCTYPE html>
<html lang="en">
<head>
<meta charset="utf-8">
<title>Marcus Lindqvist Photography — Business Card</title>
<link rel="stylesheet" href="https://fonts.googleapis.com/css2?family=Montserrat:wght@400;600&display=swap">
<style>
  :root {
    --page-bg: #d9d9da;
    --card-light: #f7f6f4;
    --card-mid: #e7e4e0;
    --ink: #1d1d1d;
    --ink-soft: #6a6a6a;
    --rule: #a9a6a2;
    --photo-dark: #4a4746;
    --photo-mid: #9a9692;
    --chip: #5a5a5a;
  }
  * { box-sizing: border-box; margin: 0; padding: 0; }
  html, body { width: 1200px; height: 871px; overflow: hidden; }
  body {
    background: var(--page-bg);
    font-family: "Montserrat", Arial, sans-serif;
    color: var(--ink);
    display: flex;
    align-items: center;
    justify-content: center;
    gap: 48px;
  }
  .card {
    position: relative;
    width: 520px;
    height: 297px;
    overflow: hidden;
    background: linear-gradient(160deg, var(--card-light) 0%, var(--card-mid) 100%);
    box-shadow: 0 6px 18px rgba(0,0,0,0.18);
  }

  .name {
    font-weight: 600;
    font-size: 24px;
    line-height: 30px;
    color: var(--ink);
    white-space: nowrap;
  }
  .role {
    font-weight: 400;
    font-size: 11px;
    line-height: 14px;
    color: var(--ink-soft);
    text-align: right;
    padding-right: 38px;
  }

  /* Front */
  .front__photo {
    position: absolute;
    left: 0; top: 0;
    width: 225px; height: 100%;
    background: linear-gradient(90deg, var(--photo-dark) 0%, var(--photo-mid) 70%, rgba(231,228,224,0) 100%);
  }
  .front__identity {
    position: absolute;
    right: 44px; top: 112px;
  }
  .front__web {
    position: absolute;
    right: 44px; bottom: 46px;
    font-size: 11.5px;
  }

  /* Back */
  .back__photo {
    position: absolute;
    right: 0; top: 0;
    width: 120px; height: 64px;
    background: linear-gradient(225deg, var(--photo-dark) 0%, var(--photo-mid) 45%, rgba(231,228,224,0) 85%);
  }
  .back__identity {
    position: absolute;
    left: 32px; top: 126px;
  }
  .back__web {
    position: absolute;
    left: 32px; top: 194px;
    font-size: 10.5px;
    line-height: 14px;
  }
  .back__rule {
    position: absolute;
    left: 0; right: 0; top: 216px;
    height: 1px;
    background: var(--rule);
  }
  .contact-list {
    position: absolute;
    list-style: none;
    font-size: 9.5px;
    line-height: 17px;
  }
  .contact-list--direct { left: 32px; top: 226px; }
  .contact-list--social { left: 300px; top: 170px; }
  .contact-list li { display: flex; align-items: center; gap: 7px; white-space: nowrap; }
  .contact-list svg { width: 11px; height: 11px; flex: none; }
  .chip {
    width: 10px; height: 10px;
    background: var(--chip);
    flex: none;
  }
</style>
</head>
<body>

  <section class="card card--front">
    <div class="front__photo" role="img" aria-label="Black and white photograph of a model lying on a flowing patterned gown"></div>
    <div class="front__identity">
      <div class="name">Marcus Lindqvist</div>
      <div class="role">photographer</div>
    </div>
    <div class="front__web">www.marcuslvqphoto.com</div>
  </section>

  <section class="card card--back">
    <div class="back__photo" role="img" aria-label="Corner detail of a dark patterned fabric photograph"></div>
    <div class="back__identity">
      <div class="name">Marcus Lindqvist</div>
      <div class="role">photographer</div>
    </div>
    <ul class="contact-list contact-list--social">
      <li><span class="chip"></span>marcus.lindqvist</li>
      <li><span class="chip"></span>@marcuslvqphoto</li>
    </ul>
    <div class="back__web">www.marcuslvqphoto.com</div>
    <div class="back__rule"></div>
    <ul class="contact-list contact-list--direct">
      <li>
        <svg viewBox="0 0 12 12" aria-hidden="true"><circle cx="6" cy="6" r="5.3" fill="none" stroke="#444" stroke-width="1"/><path d="M4.2 3.3l1 1-.6.8c.4.9 1 1.5 1.9 1.9l.8-.6 1 1-.7.9c-1.9-.3-3.9-2.3-4.2-4.2z" fill="#444"/></svg>
        +1 903 555 0142
      </li>
      <li>
        <svg viewBox="0 0 12 12" aria-hidden="true"><rect x="1" y="2.5" width="10" height="7" fill="none" stroke="#444" stroke-width="1"/><path d="M1 2.5l5 4 5-4" fill="none" stroke="#444" stroke-width="1"/></svg>
        marcus@marcuslvqphoto.com
      </li>
    </ul>
  </section>

</body>
</html>
```